A new company focused on starting and investing in transformative businesses.

We need a simple and clean website with a few pages. we like marlowvest.com as a starting point. we want the landing page to be very simple with an option to click through on the top right into INVESTOR LOGIN. then we want to be able to scroll down to see more about our company.

Target Market(s)

professional

Coding

Coded - Design and coding required

Number of Pages Required

2 page

Font styles to use
Serif
Sans Serif

Requirements
Must have
• HALVERN BUILDERS logo (attached as a file) on the top with INVESTOR LOGIN as a click through on the right. Please model the click through from marlowvest.com. The description (also written in attached file) should be on the landing page. we do not want to have to scroll to read the description.

Then we can scroll down to read more about Halvern including the mission and the two types of businesses. More is detailed on the attached file called "Halvern Website Syntax"
Should not have
• should not be slow loading with lots of fancy graphics. should not be busy and with too many colors.

```html
<!DOCTYPE html>
<html lang="en">
<head>
<meta charset="utf-8">
<title>Halvern Builders</title>
<link href="https://fonts.googleapis.com/css2?family=Nunito:wght@300;400;600;700&display=swap" rel="stylesheet">
<style>
  :root {
    --brand-blue: #02498c;
    --brand-blue-light: #b7d1ee;
    --ink: #1d1d1f;
    --white: #ffffff;
    --rule: rgba(255,255,255,0.75);
    --rule-dark: #7f9cc0;
  }
  * { margin: 0; padding: 0; box-sizing: border-box; }
  html, body { width: 985px; height: 1200px; overflow: hidden; }
  body {
    position: relative;
    background: var(--white);
    font-family: "Nunito", Arial, sans-serif;
    color: var(--ink);
  }
  .site-header .brand {
    position: absolute; left: 72px; top: 10px;
    display: flex; align-items: center; gap: 7px;
    color: var(--brand-blue); font-size: 11px; font-weight: 400;
    letter-spacing: 1px; line-height: 13px;
  }
  .brand-square { width: 18px; height: 18px; background: var(--brand-blue); }
  .investor-login {
    position: absolute; left: 790px; top: 18px;
    font-size: 13px; font-weight: 600; color: var(--brand-blue);
    text-decoration: none; padding: 0 4px; line-height: 16px;
    background: linear-gradient(transparent 55%, var(--brand-blue-light) 55%);
  }
  .hero-title {
    position: absolute; left: 100px; top: 200px; width: 785px;
    text-align: center; font-size: 33px; font-weight: 400; line-height: 38px;
  }
  .hero-title .name {
    color: var(--brand-blue);
    background: linear-gradient(transparent 72%, var(--brand-blue-light) 72%);
    padding: 0 5px 0 4px;
  }
  .hero-title .initial { font-size: 62px; line-height: 0; }
  .scroll-hint { position: absolute; left: 484px; top: 450px; }
  .about {
    position: absolute; left: 0; top: 555px; width: 985px; height: 379px;
    background: var(--brand-blue); color: var(--white);
    box-shadow: 0 4px 16px rgba(2,73,140,0.18);
  }
  .about .accent { position: absolute; }
  .mission { position: absolute; left: 72px; top: 71px; width: 320px; }
  .mission h2 { font-size: 18px; font-weight: 700; line-height: 24px; }
  .mission p { margin-top: 18px; font-size: 18px; font-weight: 400; line-height: 25.7px; }
  .focus { position: absolute; left: 492px; width: 420px; }
  .focus h3 { font-size: 18px; font-weight: 400; line-height: 24px; letter-spacing: 0.2px; }
  .focus p { margin-top: 9px; font-size: 13px; line-height: 18.5px; }
  .focus .accent { left: -16px; top: 0; }
  .ground-up { top: 71px; }
  .special { top: 218px; }
  .link-rule { position: absolute; left: 488px; top: 934px; }
  .contact { position: absolute; left: 0; top: 1027px; width: 985px; text-align: center; }
  .contact h2 {
    display: inline-block; font-size: 18px; font-weight: 400; line-height: 22px;
    padding: 0 4px; letter-spacing: 0.3px;
    background: linear-gradient(transparent 62%, var(--brand-blue-light) 62%);
  }
  .contact p { margin-top: 17px; font-size: 18px; font-weight: 300; line-height: 26px; }
</style>
</head>
<body>
  <header class="site-header">
    <div class="brand"><span class="brand-square"></span><span>HALVERN<br>BUILDERS</span></div>
    <a class="investor-login" href="#">INVESTOR LOGIN</a>
  </header>

  <h1 class="hero-title"><span class="name"><span class="initial">H</span>alvern Builders</span> Is An Entrepreneurial Firm Focused On Building And Growing Transformational Companies</h1>

  <svg class="scroll-hint" width="17" height="27" viewBox="0 0 17 27" aria-hidden="true">
    <rect x="0.5" y="0.5" width="16" height="26" rx="8" fill="none" stroke="#333" stroke-width="0.8"/>
    <line x1="8.5" y1="5" x2="8.5" y2="10" stroke="#333" stroke-width="0.8"/>
  </svg>

  <section class="about">
    <svg class="accent" style="left:77px;top:0" width="10" height="70" aria-hidden="true">
      <line x1="1" y1="0" x2="1" y2="62" stroke="var(--rule)" stroke-width="0.6"/>
      <line x1="4" y1="0" x2="4" y2="66" stroke="var(--rule)" stroke-width="0.6"/>
      <line x1="7" y1="0" x2="7" y2="70" stroke="var(--rule)" stroke-width="0.6"/>
    </svg>
    <div class="mission">
      <h2>Our Mission</h2>
      <p>Our Mission Is To<br>Build Meaningful Businesses That Create Enduring Value By Impacting People In A Measurable Way.</p>
    </div>
    <div class="focus ground-up">
      <svg class="accent" width="8" height="30" aria-hidden="true">
        <line x1="1" y1="8" x2="1" y2="30" stroke="var(--rule)" stroke-width="0.6"/>
        <line x1="4" y1="4" x2="4" y2="26" stroke="var(--rule)" stroke-width="0.6"/>
        <line x1="7" y1="0" x2="7" y2="22" stroke="var(--rule)" stroke-width="0.6"/>
      </svg>
      <h3>GROUND UP</h3>
      <p>Our Ground Up Business Applies A Proven Analytic Process To Identify Value Edge, A Form Of Competitive Advantage. We Architect Transformational Companies And Are Deliberate In Creating The Foundation Necessary To Lead An Industry.</p>
    </div>
    <div class="focus special">
      <svg class="accent" width="8" height="30" aria-hidden="true">
        <line x1="1" y1="8" x2="1" y2="30" stroke="var(--rule)" stroke-width="0.6"/>
        <line x1="4" y1="4" x2="4" y2="26" stroke="var(--rule)" stroke-width="0.6"/>
        <line x1="7" y1="0" x2="7" y2="22" stroke="var(--rule)" stroke-width="0.6"/>
      </svg>
      <h3>SPECIAL OPPORTUNITIES</h3>
      <p>We Partner With Exceptional Teams That Create Value By Transforming Lives. Our Investment Focus Includes Large Companies And Spin-Outs.</p>
    </div>
  </section>

  <svg class="link-rule" width="10" height="68" aria-hidden="true">
    <line x1="1" y1="0" x2="1" y2="60" stroke="var(--rule-dark)" stroke-width="0.6"/>
    <line x1="5" y1="0" x2="5" y2="68" stroke="var(--rule-dark)" stroke-width="0.6"/>
    <line x1="8" y1="0" x2="8" y2="62" stroke="var(--rule-dark)" stroke-width="0.6"/>
  </svg>

  <footer class="contact">
    <h2>HALVERN BUILDERS</h2>
    <p>For Media Inquiries, Please Contact<br>press@halvernbuilders.com</p>
  </footer>
</body>
</html>
```